DM - management consultant

Business card - contemporary design

Front info
Dorian Maples

(Address not necessary)
PO Box 7386
Oakmere, CA 94071

(650) 555-0143
dm@dorianmapl.es

Twitter: dmq527
Facebook: /Dorian.Maples
Linkedin: /in/dorianmaples

Back or Front
www.dorianmaples.net
Facilitation & coaching, change management, strategic partnerships, business improvement

Target Market(s)

High tech businesses - mostly startups in Silicon Valley

Industry/Entity Type

Business

Font styles to use
Sans Serif

Colors

Designer to choose colors to be used in the design.

```html
<!DOCTYPE html>
<html lang="en">
<head>
<meta charset="utf-8">
<title>Dorian Maples — Business Card</title>
<link rel="stylesheet" href="https://fonts.googleapis.com/css2?family=Questrial&display=swap">
<style>
  :root {
    --page: #e6e7e9;
    --card-blue: #0a4fa3;
    --name-grey: #9c9c9c;
    --detail-grey: #8b97a8;
    --tagline: #ffffff;
    --shade: rgba(0, 0, 0, 0.18);
  }
  * { box-sizing: border-box; margin: 0; padding: 0; }
  html, body {
    width: 1200px;
    height: 900px;
    overflow: hidden;
    background: var(--page);
    font-family: "Questrial", "Century Gothic", sans-serif;
  }
  .sheet {
    width: 1200px;
    height: 900px;
    display: flex;
    flex-direction: column;
    align-items: center;
    justify-content: center;
    gap: 24px;
  }
  .card {
    position: relative;
    width: 700px;
    height: 400px;
    background: var(--card-blue);
    box-shadow: 0 6px 18px var(--shade);
    overflow: hidden;
  }
  .sheen {
    position: absolute;
    left: 40px;
    bottom: 10px;
    width: 300px;
    height: 120px;
    background: radial-gradient(ellipse at 45% 50%, rgba(255,255,255,0.14), rgba(255,255,255,0) 70%);
  }
  /* back side */
  .tagline {
    position: absolute;
    left: 44px;
    top: 64px;
    width: 600px;
    color: var(--tagline);
    font-size: 23px;
    line-height: 1.25;
    letter-spacing: 0.2px;
  }
  .contact {
    position: absolute;
    left: 420px;
    top: 212px;
    color: var(--detail-grey);
    font-size: 16px;
    line-height: 1.75;
  }
  /* front side */
  .name {
    position: absolute;
    left: 50px;
    top: 214px;
    color: var(--name-grey);
    font-size: 50px;
    font-weight: 400;
    line-height: 60px;
    letter-spacing: 0.5px;
    white-space: nowrap;
  }
  .rule {
    position: absolute;
    left: 392px;
    top: 250px;
  }
  .website {
    position: absolute;
    left: 396px;
    top: 262px;
    color: var(--name-grey);
    font-size: 21px;
    white-space: nowrap;
  }
</style>
</head>
<body>
<main class="sheet">
  <section class="card card-back">
    <p class="tagline">Facilitation &amp; coaching, change management, strategic partnerships, business improvement</p>
    <p class="contact">PO Box 7386, Oakmere, CA 94071<br>(650) 555-0143</p>
    <div class="sheen" role="img" aria-label="Faint diagonal light streaks"></div>
  </section>

  <section class="card card-front">
    <h1 class="name">Dorian Maples</h1>
    <svg class="rule" width="280" height="8" viewBox="0 0 280 8" aria-hidden="true">
      <defs>
        <linearGradient id="rule-fade" x1="0" x2="1" y1="0" y2="0">
          <stop offset="0" stop-color="#9c9c9c"/>
          <stop offset="1" stop-color="#9c9c9c" stop-opacity="0"/>
        </linearGradient>
      </defs>
      <rect x="0" y="2" width="280" height="4" fill="url(#rule-fade)"/>
    </svg>
    <p class="website">www.dorianmaples.net</p>
    <div class="sheen" role="img" aria-label="Faint diagonal light streaks"></div>
  </section>
</main>
</body>
</html>
```